Car Repair Business Website Redesign

We need a new design for our wordpress website, which generates traffic and converts leads for our car repair business. The site was originally setup with a blank template and the design was never tweaked. All content is in place, so the design needs to arrange existing content into a visually strong, responsive layout with top priority given to conversion. You can view the existing website at www.brightlanegarageworks.com. Responsive design is extremely important - 36% of visitors are mobile and 18% tablet - so please include mobile designs.
To confirm, the brief is for PSD only, please supply designs for the following two pages:-
http://www.brightlanegarageworks.com/
http://www.brightlanegarageworks.com/clutch-replacement/
Target Market(s)
Predominantly male (75%), 25-55 year old (70%) audience.
Industry/Entity Type
Car Repair
Number of Pages Required
2 page
Font styles to use
Requirements
Must have
- Good use of colour, clear design elements. Our competitors just had a re-design which although not perfect, displays many good elements: www.gearvalet.com

```html
<!DOCTYPE html>
<html lang="en">
<head>
<meta charset="utf-8">
<title>Brightlane Garage Works</title>
<link href="https://fonts.googleapis.com/css2?family=Roboto:wght@300;400;500;700&family=Roboto+Condensed:wght@400;700&family=Open+Sans:ital,wght@0,400;0,600;1,400&display=swap" rel="stylesheet">
<style>
:root{
  --blue:#1785c4;
  --blue-dark:#0f6aa6;
  --brand:#0a6fae;
  --orange:#f59a2c;
  --orange-dark:#e8861a;
  --red:#e03333;
  --footer:#2d7ca6;
  --panel:#f0f0f0;
  --line:#dcdcdc;
  --text:#555;
  --ink:#111;
  --teal:#3e9590;
}
*{box-sizing:border-box;margin:0;padding:0}
html,body{width:1200px;height:945px;overflow:hidden;background:#fff}
body{position:relative;font-family:"Open Sans",sans-serif;color:var(--text)}
.page{position:absolute;left:15px;top:24px;width:1170px;height:896px}
.abs{position:absolute}
.brand{left:0;top:0;width:233px;height:115px;display:flex;align-items:center;gap:10px;padding-left:4px}
.brand-mark{width:14px;height:14px;border-radius:50%;background:var(--brand);flex:none}
.brand-name{font-family:"Roboto",sans-serif;font-weight:700;font-size:22px;line-height:1.1;color:var(--ink)}
.nav{left:233px;top:0;width:703px;height:115px;display:flex}
.nav a{flex:1;background:linear-gradient(var(--blue),var(--blue-dark));color:#fff;text-decoration:none;border-right:1px solid #5fb0df;display:flex;flex-direction:column;align-items:center;justify-content:flex-end;padding-bottom:20px;font-family:"Roboto",sans-serif;font-weight:500;font-size:19px;gap:14px}
.nav a:last-child{border-right:0}
.contact{left:937px;top:0;width:233px;height:115px;background:var(--panel);border:1px solid var(--line);text-align:right;padding:18px 24px 0 0}
.social{display:flex;justify-content:flex-end;gap:8px;margin-bottom:10px}
.social span{width:28px;height:28px;border-radius:50%;background:#2a7bc0}
.social span:nth-child(2){background:#3ea3dd}
.social span:nth-child(3){background:#237fa8}
.contact .call{font-size:15px;color:#666;font-family:"Open Sans",sans-serif}
.contact .phone{font-family:"Roboto",sans-serif;font-weight:500;font-size:23px;color:var(--brand)}
.branch{left:0;top:115px;width:233px;height:97px;background:linear-gradient(var(--orange),var(--orange-dark));color:#fff;font-family:"Roboto",sans-serif;font-weight:500;font-size:19px;text-align:center;padding-top:21px;line-height:27px}
.map{left:0;top:212px;width:233px;height:369px;border:1px solid var(--line);border-top:0;display:flex;align-items:center;justify-content:center}
.map div{width:200px;height:300px;border-radius:40% 50% 45% 40%;background:linear-gradient(160deg,#9fb4df,#3c5fb0)}
.search{left:0;top:581px;width:233px;height:48px;background:var(--panel);border:1px solid var(--line);display:flex;align-items:center;justify-content:space-between;padding:0 16px 0 18px;font-size:14px;color:#666}
.tile{width:352px;height:168px;color:#fff;padding:24px 0 0 24px;font-family:"Roboto",sans-serif}
.tile .num{font-family:"Roboto Condensed",sans-serif;font-weight:700;font-size:60px;line-height:56px}
.tile .title{font-size:32px;font-weight:700;margin-top:6px;letter-spacing:.5px}
.tile .title span{font-weight:300}
.tile .more{font-size:13px;margin-top:6px;padding-left:4px}
.t1{left:233px;top:115px;background:linear-gradient(120deg,#e35c5c,#d03b3b 60%,#c44)}
.t2{left:585px;top:115px;background:linear-gradient(120deg,#3f9d94,#2f8a88 60%,#5aa79f)}
.t3{left:233px;top:283px;background:linear-gradient(120deg,#8ea95a,#7a9a45 60%,#6b8a3a)}
.t4{left:585px;top:283px;background:linear-gradient(120deg,#1f6fa5,#165c8f 60%,#2a7cb0)}
.reviews{left:233px;top:451px;width:704px;height:178px;border:1px solid var(--line);border-top:0}
.reviews h2{position:absolute;left:30px;top:26px;font-family:"Roboto",sans-serif;font-weight:500;font-size:20px;color:var(--brand)}
.arrows{position:absolute;right:26px;top:26px;color:#aaa;font-size:14px;letter-spacing:6px}
.avatar{position:absolute;left:35px;top:64px;width:93px;height:93px;border-radius:50%;background:radial-gradient(circle at 50% 40%,#ddd,#555 60%,#222)}
.quote{position:absolute;left:170px;top:77px;width:500px;font-style:italic;font-size:12.5px;line-height:26px;color:#666}
.qm{position:absolute;font-family:Georgia,serif;font-size:22px;color:#777;font-weight:700}
.help{left:937px;top:115px;width:233px;height:57px;background:linear-gradient(var(--orange),var(--orange-dark));color:#fff;font-family:"Roboto",sans-serif;font-weight:500;font-size:19px;padding:15px 0 0 23px}
.help-item{left:937px;width:233px;height:58px;background:var(--panel);border:1px solid var(--line);border-top:0;display:flex;align-items:center;gap:14px;padding-left:20px;font-size:15px;color:#555}
.why{left:937px;top:346px;width:233px;height:104px;background:linear-gradient(var(--orange),var(--orange-dark));color:#fff;font-family:"Roboto",sans-serif;font-weight:500;font-size:19px;text-align:center;padding-top:24px;line-height:27px}
.why-list{left:937px;top:450px;width:233px;height:179px;border:1px solid var(--line);border-top:0;list-style:none;padding:20px 0 0 18px}
.why-list li{display:flex;align-items:center;gap:7px;font-size:13px;color:#666;height:38px}
.bar{top:631px;height:42px;background:var(--red);color:#fff;font-family:"Roboto",sans-serif;font-weight:700;font-size:14px;padding:14px 0 0 20px}
.clutch{left:0;top:673px;width:584px;height:142px;background:var(--panel);border:1px solid var(--line)}
.clutch p{position:absolute;left:168px;top:27px;width:380px;font-size:13px;line-height:28px;color:#666}
.faq{left:585px;top:673px;width:585px;height:142px;background:var(--panel);border:1px solid var(--line);display:flex;gap:14px;padding:17px 0 0 17px}
.faq figure{width:99px}
.faq .ph{width:99px;height:80px}
.faq figcaption{font-size:12.5px;color:#666;margin-top:8px}
.footer{left:0;top:819px;width:1170px;height:77px;background:var(--footer);color:#fff;display:flex;align-items:center;justify-content:space-between;padding:0 37px 0 36px;font-size:13px}
.footer nav span{margin:0 22px}
</style>
</head>
<body>
<div class="page">
  <div class="abs brand"><span class="brand-mark"></span><span class="brand-name">Brightlane Garage Works</span></div>

  <nav class="abs nav">
    <a href="#"><svg width="46" height="40" viewBox="0 0 46 40" fill="#fff"><circle cx="16" cy="22" r="11"/><circle cx="33" cy="11" r="7"/><circle cx="35" cy="30" r="6"/><circle cx="16" cy="22" r="4" fill="#1785c4"/><circle cx="33" cy="11" r="2.5" fill="#1785c4"/><circle cx="35" cy="30" r="2" fill="#1785c4"/></svg>SERVICES</a>
    <a href="#"><svg width="40" height="40" viewBox="0 0 40 40"><circle cx="20" cy="20" r="17" fill="#fff"/><path d="M12 10c5 2 6 7 3 10s2 8 0 12M26 8c-2 5 5 7 8 9M24 26c3-2 6 1 6 4" stroke="#1785c4" stroke-width="3" fill="none"/></svg>LOCATIONS</a>
    <a href="#"><svg width="44" height="42" viewBox="0 0 44 42"><path d="M22 2C11 2 2 9 2 18c0 6 3 10 8 13l-2 9 9-6c2 0 3 1 5 1 11 0 20-8 20-17S33 2 22 2z" fill="#fff"/><text x="22" y="27" text-anchor="middle" font-family="Roboto,sans-serif" font-weight="700" font-size="20" fill="#1785c4">?</text></svg>FAQ'S</a>
    <a href="#"><svg width="42" height="38" viewBox="0 0 42 38" fill="#fff"><circle cx="9" cy="9" r="5"/><circle cx="21" cy="7" r="6"/><circle cx="33" cy="9" r="5"/><rect x="2" y="16" width="14" height="12" rx="5"/><rect x="26" y="16" width="14" height="12" rx="5"/><circle cx="21" cy="20" r="5"/><rect x="11" y="25" width="20" height="13" rx="6"/></svg>ABOUT US</a>
  </nav>

  <div class="abs contact">
    <div class="social"><span></span><span></span><span></span></div>
    <div class="call">Call us today</div>
    <div class="phone">0800 555 0142</div>
  </div>

  <div class="abs branch">FIND YOUR<br>CLOSEST BRANCH</div>
  <div class="abs map"><div role="img" aria-label="Map of the UK and Ireland showing branch regions"></div></div>
  <div class="abs search">City/Postcode
    <svg width="18" height="18" viewBox="0 0 18 18"><circle cx="7.5" cy="7.5" r="5.5" stroke="#999" stroke-width="2.4" fill="none"/><path d="M11.5 11.5l5 5" stroke="#999" stroke-width="2.6"/></svg></div>

  <a class="abs tile t1" role="img" aria-label="Red sports car photo"><div class="num">01</div><div class="title">INSTANT <span>QUOTE</span></div><div class="more">CLICK HERE FOR MORE INFO »</div></a>
  <a class="abs tile t2" role="img" aria-label="Refuelling a car photo"><div class="num">02</div><div class="title">INSTANT <span>QUOTE</span></div><div class="more">CLICK HERE FOR MORE INFO »</div></a>
  <a class="abs tile t3" role="img" aria-label="Customer and mechanic meeting photo"><div class="num">03</div><div class="title">INSTANT <span>QUOTE</span></div><div class="more">CLICK HERE FOR MORE INFO »</div></a>
  <a class="abs tile t4" role="img" aria-label="Woman on a phone call photo"><div class="num">04</div><div class="title">INSTANT <span>QUOTE</span></div><div class="more">CLICK HERE FOR MORE INFO »</div></a>

  <section class="abs reviews">
    <h2>PREVIOUS CUSTOMERS'S REVIEWS</h2>
    <div class="arrows">‹ ›</div>
    <div class="avatar" role="img" aria-label="Customer portrait"></div>
    <span class="qm" style="left:146px;top:66px">“</span>
    <p class="quote">Simply dummy text of the printing and typesetting industry. Lorem Ipsum has been the industry's standard dummy text ever since the 1500s, when an unknown printer took a galley of type and scrambled...</p>
    <span class="qm" style="left:664px;top:132px">”</span>
  </section>

  <div class="abs help">NEED HELP?</div>
  <div class="abs help-item" style="top:172px"><svg width="34" height="26" viewBox="0 0 34 26" fill="none" stroke="#2a8fc4" stroke-width="2"><ellipse cx="13" cy="10" rx="11" ry="8"/><path d="M6 16l-3 6 7-4M22 7c6 1 10 4 10 8 0 2-1 4-3 5l2 5-6-3"/></svg>Chat with Us</div>
  <div class="abs help-item" style="top:230px"><svg width="30" height="28" viewBox="0 0 30 28"><path d="M5 2l6 0 2 7-4 3c2 5 5 8 10 10l3-4 7 2v6c-14 1-25-10-24-24z" fill="#2a8fc4"/></svg>Request a Call Back</div>
  <div class="abs help-item" style="top:288px"><svg width="30" height="32" viewBox="0 0 30 32" fill="none" stroke="#2a8fc4" stroke-width="2"><path d="M4 2h15l7 7v21H4z M19 2v7h7 M9 15h12M9 20h12M9 25h12"/></svg>Ask for a Quote</div>
  <div class="abs why">WHY ARE WE THE<br>BEST CHOICE?</div>
  <ul class="abs why-list">
    <li><svg width="15" height="13" viewBox="0 0 15 13" fill="none" stroke="#e8661a" stroke-width="1.6"><path d="M1 6h3v6H1zM4 6l3-5h1v4h6v2l-2 5H4"/></svg>Simply dummy text printing</li>
    <li><svg width="15" height="13" viewBox="0 0 15 13" fill="none" stroke="#e8661a" stroke-width="1.6"><path d="M1 6h3v6H1zM4 6l3-5h1v4h6v2l-2 5H4"/></svg>Simply dummy text</li>
    <li><svg width="15" height="13" viewBox="0 0 15 13" fill="none" stroke="#e8661a" stroke-width="1.6"><path d="M1 6h3v6H1zM4 6l3-5h1v4h6v2l-2 5H4"/></svg>Simply dummy</li>
    <li><svg width="15" height="13" viewBox="0 0 15 13" fill="none" stroke="#e8661a" stroke-width="1.6"><path d="M1 6h3v6H1zM4 6l3-5h1v4h6v2l-2 5H4"/></svg>Simply dummy text printing</li>
  </ul>

  <div class="abs bar" style="left:0;width:584px">DO I NEED A CLUTCH REPLACEMENT?</div>
  <div class="abs bar" style="left:585px;width:585px">FREQUENTLY ASKED QUESTIONS</div>

  <section class="abs clutch">
    <svg style="position:absolute;left:36px;top:27px" width="90" height="84" viewBox="0 0 90 84" fill="var(--teal)">
      <g><circle cx="30" cy="42" r="21"/><rect x="25" y="14" width="10" height="56"/><rect x="2" y="37" width="56" height="10"/><rect x="25" y="14" width="10" height="56" transform="rotate(45 30 42)"/><rect x="25" y="14" width="10" height="56" transform="rotate(-45 30 42)"/><circle cx="30" cy="42" r="9" fill="#f0f0f0"/></g>
      <g><circle cx="72" cy="18" r="11"/><rect x="69" y="3" width="6" height="30"/><rect x="57" y="15" width="30" height="6"/><rect x="69" y="3" width="6" height="30" transform="rotate(45 72 18)"/><rect x="69" y="3" width="6" height="30" transform="rotate(-45 72 18)"/><circle cx="72" cy="18" r="4.5" fill="#f0f0f0"/></g>
      <g><circle cx="72" cy="64" r="11"/><rect x="69" y="49" width="6" height="30"/><rect x="57" y="61" width="30" height="6"/><rect x="69" y="49" width="6" height="30" transform="rotate(45 72 64)"/><rect x="69" y="49" width="6" height="30" transform="rotate(-45 72 64)"/><circle cx="72" cy="64" r="4.5" fill="#f0f0f0"/></g>
    </svg>
    <p>Simply dummy text of the printing and typesetting industry. Lorem Ipsum has been the industry's standard dummy text ever since the 1500s, when an unknown printer...</p>
  </section>

  <section class="abs faq">
    <figure><div class="ph" role="img" aria-label="Person reviewing paperwork" style="background:linear-gradient(135deg,#d8d8d8,#8a7a70)"></div><figcaption>Simply dummy</figcaption></figure>
    <figure><div class="ph" role="img" aria-label="Businessman in an office" style="background:linear-gradient(135deg,#8fc3e8,#2a4e7a)"></div><figcaption>Simply dummy</figcaption></figure>
    <figure><div class="ph" role="img" aria-label="Laptop and coffee on a desk" style="background:linear-gradient(135deg,#e8dcc0,#8a7d66)"></div><figcaption>Simply dummy</figcaption></figure>
    <figure><div class="ph" role="img" aria-label="Silver car on the road" style="background:linear-gradient(135deg,#cfd3d6,#5c6266)"></div><figcaption>Simply dummy</figcaption></figure>
    <figure><div class="ph" role="img" aria-label="Hands with a tablet and documents" style="background:linear-gradient(135deg,#e9a650,#2a5aa0)"></div><figcaption>Simply dummy</figcaption></figure>
  </section>

  <footer class="abs footer">
    <nav>Home<span>/</span>Services<span>/</span>Locations<span>/</span>Faq's<span>/</span>About us</nav>
    <div>© Copyrights 2015. Brightlane garage works. All rights reserved.</div>
  </footer>
</div>
</body>
</html>
```